Stationery Design for Family Law Firm
BROOK VESTAL, LLP
Stationery Design for Family Law Firm -
Creative Brief
Professional
Martin D. Vestal
Attorney & Counselor at Law
4187 Larkin Street San Diego, CA 92104
martin@brookvestal-law.example
www.brookvestal-law.example
Paper will be ivory. Please use large and small caps for name and "Attorney & Counselor" at Law. Sentence case for the rest.
Family Law I Guardianships I Conservatorships I Estate Planning

```html
<!DOCTYPE html>
<html lang="en">
<head>
<meta charset="utf-8">
<title>Brook Vestal, LLP — Business Card</title>
<link href="https://fonts.googleapis.com/css2?family=Source+Sans+3:wght@400;600;700&display=swap" rel="stylesheet">
<style>
  :root {
    --backdrop: #3b3b3d;
    --blue-light: #3b8bd0;
    --blue-mid: #1d64a8;
    --blue-dark: #0d3f78;
    --paper: #ffffff;
    --ink-white: #ffffff;
    --brand-blue: #1f5f9f;
    --rule-blue: #2a6fb0;
  }
  * { margin: 0; padding: 0; box-sizing: border-box; }
  html, body { width: 1200px; height: 780px; overflow: hidden; }
  body {
    background: var(--backdrop);
    font-family: "Source Sans 3", "Myriad Pro", sans-serif;
    position: relative;
  }
  .business-card {
    position: absolute;
    left: 100px; top: 105px;
    width: 1000px; height: 570px;
    border-radius: 26px;
    overflow: hidden;
    background: var(--paper);
    box-shadow: 0 10px 30px rgba(0,0,0,0.45);
    display: flex;
  }
  .contact-panel {
    position: relative;
    width: 432px;
    height: 100%;
    background: radial-gradient(circle at 42% 38%, var(--blue-light) 0%, var(--blue-mid) 45%, var(--blue-dark) 100%);
    color: var(--ink-white);
    padding: 96px 0 0 46px;
  }
  .divider {
    width: 12px;
    height: 100%;
    background: var(--paper);
    position: relative;
  }
  .divider::after {
    content: "";
    position: absolute;
    left: 4px; top: 0; bottom: 0;
    width: 3px;
    background: var(--rule-blue);
  }
  .attorney-name {
    font-size: 31px;
    font-weight: 700;
    letter-spacing: 0.2px;
    line-height: 1.1;
  }
  .attorney-title {
    font-size: 20px;
    font-weight: 600;
    margin-top: 6px;
  }
  .contact-block {
    position: absolute;
    left: 46px; top: 378px;
    font-size: 17px;
  }
  .address { margin-bottom: 30px; }
  .contact-line {
    display: flex;
    align-items: center;
    gap: 10px;
    height: 30px;
  }
  .contact-line svg { width: 16px; height: 16px; flex: none; }
  .brand-panel {
    flex: 1;
    display: flex;
    align-items: center;
    justify-content: center;
    gap: 16px;
  }
  .brand-mark {
    width: 22px; height: 22px;
    background: var(--brand-blue);
  }
  .brand-name {
    color: var(--brand-blue);
    font-size: 44px;
    font-weight: 700;
    letter-spacing: 1px;
  }
</style>
</head>
<body>
  <div class="business-card">
    <section class="contact-panel">
      <h1 class="attorney-name">Martin D. Vestal</h1>
      <p class="attorney-title">Attorney &amp; Counselor at Law</p>
      <div class="contact-block">
        <p class="address">4187 Larkin Street San Diego, CA 92104</p>
        <p class="contact-line">
          <svg viewBox="0 0 24 24" aria-hidden="true"><path fill="#fff" d="M6.6 10.8c1.4 2.8 3.8 5.1 6.6 6.6l2.2-2.2c.3-.3.7-.4 1-.2 1.1.4 2.3.6 3.6.6.6 0 1 .4 1 1V20c0 .6-.4 1-1 1C10.6 21 3 13.4 3 4c0-.6.4-1 1-1h3.5c.6 0 1 .4 1 1 0 1.3.2 2.5.6 3.6.1.3 0 .7-.2 1z"/></svg>
          <span>(619) 555-0148</span>
        </p>
        <p class="contact-line">
          <svg viewBox="0 0 24 24" aria-hidden="true"><circle cx="12" cy="12" r="4" fill="none" stroke="#fff" stroke-width="2.4"/><path d="M16 8v5.5a2.5 2.5 0 0 0 5 0V12a9 9 0 1 0-3.5 7.1" fill="none" stroke="#fff" stroke-width="2.4"/></svg>
          <span>martin@brookvestal-law.example</span>
        </p>
        <p class="contact-line">
          <svg viewBox="0 0 24 24" aria-hidden="true"><circle cx="12" cy="12" r="9.5" fill="none" stroke="#fff" stroke-width="2"/><ellipse cx="12" cy="12" rx="4" ry="9.5" fill="none" stroke="#fff" stroke-width="1.6"/><path d="M2.5 12h19M4 7h16M4 17h16" stroke="#fff" stroke-width="1.4"/></svg>
          <span>www.brookvestal-law.example</span>
        </p>
      </div>
    </section>
    <div class="divider"></div>
    <section class="brand-panel">
      <span class="brand-mark"></span>
      <span class="brand-name">BROOK VESTAL, LLP</span>
    </section>
  </div>
</body>
</html>
```